Residential technology services business card

Looking for a simple, catchy, slightly fun business card design.

We are a residential technology service provider (computer repair, tablet repair, training, etc). We are a fun, upbeat, yet professional company that is very skilled at our job.

I will upload our logo in a sec, thinking that it should be the only thing on the front side of the card, with maybe a punch line as well... maybe not. Maybe the punchline can find a place on the back. You be the judge.

Backside should be minimal in terms of information. I need two variations: one that will only have our website and phone and one that will also include a persons name (and position), personal e-mail and personal phone.

Well, you're the designer, figure out the best way to place all above mentioned items.

Colors are white, black, green (as in logo), plus whatever else you think needs adding (if any).

It must be clear to people what we do (provide computer services, tablet services)... without using generic pictures of computers and tablets, unless it 's something original.

We want something original! But do note that the card will be printed on standard size business card paper, so no funky shapes please.

Thanks!!!

Residential

Requirements
Must have
• Logo, website, phone.
2nd variation also must include space for persons name, personal phone and email.

```html
<!DOCTYPE html>
<html lang="en">
<head>
<meta charset="utf-8">
<title>NimbleByte – Business Card</title>
<link rel="stylesheet" href="https://fonts.googleapis.com/css2?family=Arimo:wght@400;700&display=swap">
<style>
  :root {
    --backdrop: #b9b9b9;
    --card-black: #0b0b0b;
    --card-white: #ffffff;
    --brand-green: #7ac943;
    --ink: #1a1a1a;
    --ink-soft: #333333;
  }
  * { box-sizing: border-box; margin: 0; padding: 0; }
  html, body { width: 1200px; height: 900px; overflow: hidden; }
  body {
    background: var(--backdrop);
    font-family: "Arimo", Arial, sans-serif;
    position: relative;
  }
  .card {
    position: absolute;
    width: 525px;
    height: 300px;
    overflow: hidden;
    box-shadow: 0 10px 24px rgba(0,0,0,0.25);
  }
  .card--front { left: 50px; top: 300px; background: var(--card-black); }
  .card--back { left: 625px; top: 300px; background: var(--card-white); }

  .brand {
    position: absolute;
    display: flex;
    align-items: center;
    gap: 14px;
    font-weight: 700;
    letter-spacing: -1px;
  }
  .brand__dot {
    width: 22px; height: 22px; border-radius: 50%;
    background: var(--brand-green);
    flex: none;
  }
  .card--front .brand {
    left: 0; right: 0; top: 0; bottom: 0;
    justify-content: center;
    font-size: 58px;
    color: var(--card-white);
  }
  .card--back .brand {
    left: 34px; top: 168px;
    font-size: 44px;
    color: var(--ink);
  }

  .person { position: absolute; left: 300px; top: 44px; }
  .person__name { font-size: 15px; color: var(--ink); }
  .person__role { font-size: 15px; color: var(--brand-green); margin-top: 2px; }

  .contact {
    position: absolute; left: 340px; top: 118px;
    list-style: none; font-size: 11.5px; line-height: 16px; color: var(--ink-soft);
  }

  .edge-band { position: absolute; }
  .edge-band--bottom { left: 0; right: 0; bottom: 0; height: 9px; background: var(--brand-green); }
  .edge-band--tick { right: 0; top: 18px; width: 7px; height: 22px; background: var(--brand-green); }
  .edge-band--side { right: 0; top: 128px; width: 22px; bottom: 9px; background: var(--card-black); }
  .edge-band--side-cap { right: 22px; top: 128px; width: 6px; height: 42px; background: var(--brand-green); }
</style>
</head>
<body>
  <section class="card card--front" aria-label="Card front">
    <div class="brand"><span class="brand__dot"></span>NimbleByte</div>
  </section>

  <section class="card card--back" aria-label="Card back">
    <div class="brand"><span class="brand__dot"></span>NimbleByte</div>
    <div class="person">
      <p class="person__name">Dana Mercer</p>
      <p class="person__role">Manager</p>
    </div>
    <ul class="contact">
      <li>+0 987 654 321</li>
      <li>dana@nimblebyte.com</li>
      <li>www.nimblebyte.com</li>
    </ul>
    <span class="edge-band edge-band--tick"></span>
    <span class="edge-band edge-band--side"></span>
    <span class="edge-band edge-band--side-cap"></span>
    <span class="edge-band edge-band--bottom"></span>
  </section>
</body>
</html>
```